I already have a logo created by Sketch Harbor that I'm very happy with. I need to spruce up my business card now. Its a double sided card with not much info on it, I like to keep it simple.
Front of card: name, phone # email address, web address. Tag Line "Outsourced Technology Solutions", under that it says Business Voice Services & Electronic Protection.
Rear of Card: Content written inside a "cloud" saying "Cloud Solutions" "Cloud Integrity"

Target Market(s)

Business to Business

Industry/Entity Type

Business

Contact Information for Business Card

We are in the technology field. Providing Telephone systems (hardware), SIP Trunks (dial tone/local/long distance/telephone #'s), LAN (Local Area Network)infrastructure cabling, Data Center solutions and Security Applications (Camera systems, Access Control systems,

Requirements
Must have
• Must have brevity
Should not have
• Clutter and/or too much information

```html
<!DOCTYPE html>
<html lang="en">
<head>
<meta charset="utf-8">
<title>Northvale Connect – Business Card</title>
<link rel="stylesheet" href="https://fonts.googleapis.com/css2?family=Open+Sans:wght@400;600;700&display=swap">
<style>
  :root {
    --navy: #1f4591;
    --ink: #3a3a3a;
    --grey: #8a8a8a;
    --paper: #ffffff;
    --backdrop: #2b2e33;
  }
  * { margin: 0; padding: 0; box-sizing: border-box; }
  html, body { width: 1200px; height: 900px; overflow: hidden; }
  body {
    background: var(--backdrop);
    font-family: "Open Sans", Arial, sans-serif;
    position: relative;
  }
  .card {
    position: absolute;
    top: 295px;
    width: 540px;
    height: 310px;
    background: var(--paper);
    border-radius: 22px;
    overflow: hidden;
  }
  .card--front { left: 40px; }
  .card--back { left: 620px; }

  /* Brand block */
  .brand { color: var(--navy); }
  .brand__name {
    display: flex;
    align-items: center;
    gap: 10px;
    font-weight: 700;
    font-size: 20px;
    line-height: 1.1;
    color: var(--navy);
  }
  .brand__mark {
    width: 16px; height: 16px;
    background: var(--navy);
    flex: none;
  }
  .brand__tagline {
    margin-top: 6px;
    padding-top: 4px;
    border-top: 1px solid var(--grey);
    font-size: 11px;
    color: var(--grey);
    letter-spacing: .2px;
  }

  /* Front */
  .card--front .brand {
    position: absolute;
    left: 34px;
    top: 44px;
  }
  .name-band {
    position: absolute;
    left: 250px;
    right: 0;
    top: 140px;
    height: 58px;
    background: var(--navy);
    color: var(--paper);
    padding: 7px 0 0 22px;
  }
  .name-band__name {
    font-weight: 700;
    font-size: 22px;
    letter-spacing: .5px;
    line-height: 1.1;
  }
  .name-band__role {
    font-size: 14px;
    font-weight: 600;
    letter-spacing: .6px;
  }
  .contacts {
    position: absolute;
    left: 254px;
    top: 212px;
    list-style: none;
    font-size: 13px;
    color: var(--ink);
    line-height: 1.35;
  }
  .contacts__item {
    display: flex;
    align-items: flex-start;
    gap: 9px;
    margin-bottom: 3px;
  }
  .contacts__icon {
    width: 13px; height: 13px;
    flex: none;
    margin-top: 3px;
    fill: var(--navy);
  }

  /* Back */
  .back-frame {
    position: absolute;
    inset: 18px;
    border: 1.5px solid var(--navy);
    border-radius: 16px;
  }
  .card--back .brand {
    position: absolute;
    left: 50%;
    top: 112px;
    transform: translateX(-50%);
  }
  .back-web {
    position: absolute;
    left: 50%;
    bottom: 10px;
    transform: translateX(-50%);
    background: var(--paper);
    padding: 0 12px;
    font-size: 13px;
    color: var(--navy);
    white-space: nowrap;
  }
</style>
</head>
<body>

  <section class="card card--front">
    <div class="brand">
      <div class="brand__name"><span class="brand__mark"></span>Northvale Connect, LLC</div>
      <div class="brand__tagline">Outsourced Technology Solutions</div>
    </div>

    <div class="name-band">
      <div class="name-band__name">DANIEL REYES</div>
      <div class="name-band__role">Software Engineer</div>
    </div>

    <ul class="contacts">
      <li class="contacts__item">
        <svg class="contacts__icon" viewBox="0 0 24 24"><path d="M6.6 10.8a15.1 15.1 0 0 0 6.6 6.6l2.2-2.2a1 1 0 0 1 1-.25 11.4 11.4 0 0 0 3.6.57 1 1 0 0 1 1 1V20a1 1 0 0 1-1 1A17 17 0 0 1 3 4a1 1 0 0 1 1-1h3.5a1 1 0 0 1 1 1c0 1.25.2 2.45.57 3.57a1 1 0 0 1-.25 1z"/></svg>
        +000 12345 6789
      </li>
      <li class="contacts__item">
        <svg class="contacts__icon" viewBox="0 0 24 24"><path d="M2 5h20v14H2z M3.5 6.5 12 13l8.5-6.5" fill="none" stroke="#1f4591" stroke-width="2"/></svg>
        urname@email.com
      </li>
      <li class="contacts__item">
        <svg class="contacts__icon" viewBox="0 0 24 24"><circle cx="12" cy="12" r="9.5" fill="none" stroke="#1f4591" stroke-width="2"/><path d="M2.5 12h19M12 2.5c-5 5-5 14 0 19M12 2.5c5 5 5 14 0 19" fill="none" stroke="#1f4591" stroke-width="1.6"/></svg>
        urwebsitename.com
      </li>
      <li class="contacts__item">
        <svg class="contacts__icon" viewBox="0 0 24 24"><path d="M12 2a7 7 0 0 0-7 7c0 5.2 7 13 7 13s7-7.8 7-13a7 7 0 0 0-7-7zm0 9.5A2.5 2.5 0 1 1 12 6.5a2.5 2.5 0 0 1 0 5z"/></svg>
        <span>Your Street Address<br>Singapore, 1234</span>
      </li>
    </ul>
  </section>

  <section class="card card--back">
    <div class="back-frame"></div>
    <div class="brand">
      <div class="brand__name"><span class="brand__mark"></span>Northvale Connect, LLC</div>
      <div class="brand__tagline">Outsourced Technology Solutions</div>
    </div>
    <div class="back-web">yourwebsitename.com</div>
  </section>

</body>
</html>
```